Package/Product Design: Fullora 100% Scalp Coverage Powders

Need to design "high style" box and product disc design. Open to any and all suggestions. We sell 800+ skus a month on Vendexa and looking to take our box design to the next level so that we can sell even more with new look. Our competition is https://www.crownvell.com/ and https://www.sablunex.com/ I know Crownvell has a ton of money,,, but their products look "high touch, high style" and that is what we are going after. The compact has to have the ingredients on the back, same as the box. So looking for a design that makes the packaging look sleek, and still gets out point across. Logo should be in White or Black.

Target Market(s)

We sell to individuals who are experiencing hair loss, thinning hair, or gray/balding hair. This product creates the illusion of hair and allows clients get gain back confidence.

We sell on Vendexa (search fullora or scalp concealer), and www.fullorahairdust.example

Industry/Entity Type

Hair And Beauty

Logo Text

Fullora 100% Scalp Coverage Powders

Colors

Designer to choose colors to be used in the design.

Requirements
Must have
• Quality/high touch/high feel look to the packaging. Open to any and all suggestions.

```html
<!DOCTYPE html>
<html lang="en">
<head>
<meta charset="utf-8">
<title>Fullora 100% Scalp Coverage Powders – Packaging</title>
<link href="https://fonts.googleapis.com/css2?family=Poppins:wght@400;600;700&family=Tinos:ital,wght@0,400;0,700;1,400&display=swap" rel="stylesheet">
<style>
  :root{
    --canvas:#ffffff;
    --box:#0b0b0b;
    --ink:#111111;
    --paper:#ffffff;
    --body-grey:#bdbdbd;
    --warn:#d8141b;
    --gold:#f2c21a;
    --silver:#c9c9cc;
    --powder:#6a4330;
  }
  *{margin:0;padding:0;box-sizing:border-box}
  html,body{width:1200px;height:1000px;overflow:hidden;background:var(--canvas)}
  .canvas{position:relative;width:1200px;height:1000px;background:var(--canvas);font-family:"Poppins",sans-serif;color:var(--ink)}

  .brand-header{position:absolute;left:0;top:150px;width:1200px;text-align:center}
  .brand-header .wordmark{font-family:"Poppins",sans-serif;font-weight:700;font-size:100px;line-height:1;color:var(--ink);letter-spacing:-1px}
  .brand-header .tagline{font-weight:600;font-size:17px;margin-top:6px;padding-left:40px}

  .panel{position:absolute;top:330px;width:350px;height:440px;background:var(--box);color:var(--paper)}
  .panel-back{left:130px;padding:40px 22px 0}
  .panel-front{left:510px}

  .mini-brand{display:flex;align-items:center;justify-content:center;gap:10px}
  .mini-brand .compact-thumb{width:58px;height:40px;border-radius:50%;background:radial-gradient(circle,var(--powder) 55%,var(--silver) 58%)}
  .mini-brand .name{font-weight:700;font-size:30px;line-height:1}
  .mini-brand .sub{font-size:7px;text-align:right}

  .benefits h2{font-family:"Tinos",serif;font-weight:700;font-size:13px;text-align:center;margin:18px 0 8px}
  .benefits p{font-family:"Tinos",serif;font-size:9.4px;line-height:1.35;color:var(--body-grey);text-align:justify;margin-bottom:8px}
  .ingredients{font-family:"Tinos",serif;font-size:6.5px;line-height:1.3;color:var(--body-grey);margin-top:6px}
  .ingredients strong{display:block;font-style:italic;font-size:7px;color:var(--paper)}
  .back-foot{display:flex;gap:14px;margin-top:10px;font-family:"Tinos",serif;font-size:6.5px;line-height:1.35}
  .back-foot .warning{color:var(--warn);font-size:8.5px;flex:1.2}
  .back-foot .address{color:var(--body-grey);flex:1}

  .front-brand{position:absolute;left:0;top:78px;width:350px;text-align:center}
  .front-brand .name{font-weight:700;font-size:62px;line-height:1}
  .front-brand .sub{font-weight:600;font-size:11px;margin-top:2px}
  .front-compact{position:absolute;left:192px;top:160px;width:120px;height:150px;border-radius:40px;background:linear-gradient(160deg,#8f8f94,var(--powder) 55%,#2a2a2a)}
  .claims{position:absolute;left:24px;top:215px;font-weight:600;font-size:13px;line-height:1.85;letter-spacing:.5px}
  .claims li{list-style:none}
  .swatches{position:absolute;left:158px;top:303px;display:flex;gap:8px}
  .swatches span{width:27px;height:27px;border-radius:50%;border:2px solid var(--silver)}
  .s1{background:#6b4326}.s2{background:#3d3d3b}.s3{background:#56473c}.s4{background:#5e3f2a}.s5{background:#7a6238}
  .availability{position:absolute;left:48px;top:372px;font-family:"Tinos",serif;font-size:12px;color:var(--gold)}
  .net-weight{position:absolute;left:196px;top:398px;font-size:11px;color:#8a8a8a}

  .product-photo{position:absolute;left:870px;top:555px;width:260px;height:350px;border-radius:18px;background:linear-gradient(170deg,#e6e6e8,var(--silver) 40%,var(--powder) 75%,#4a3024)}
  .applicator-photo{position:absolute;left:650px;top:790px;width:150px;height:120px;border-radius:10px;background:linear-gradient(180deg,#f2f2f2 30%,#1a1a1a 32%)}
</style>
</head>
<body>
<main class="canvas">
  <header class="brand-header">
    <div class="wordmark">Fullora</div>
    <div class="tagline">100% scalp coverage</div>
  </header>

  <section class="panel panel-back" aria-label="Box back panel">
    <div class="mini-brand">
      <div class="compact-thumb" role="img" aria-label="Small photo of the open powder compact"></div>
      <div><div class="name">Fullora</div><div class="sub">100% scalp coverage</div></div>
    </div>
    <div class="benefits">
      <h2>Fullora Hair Powder Benefits</h2>
      <p>Fullora 100% Scalp Coverage fills in balding or thinning spots and looks like natural growing hair. Fullora 100% Scalp Coverage is great for those in-between color weeks outside of the salon or also to use on cowlicks which cause separation on the hair. Fullora 100% Scalp Coverage is available in five colors which will blend well with any color hair or even mix two colors together to achieve a blended color look for highlighted or salt and pepper hair. Fullora 100% Scalp Coverage is water insoluble and talc-free.</p>
      <p>100% Scalp Coverage Fullora 100% Scalp coverage is a talc-free product that completely covers gray hair, fills in bald spots, and helps thinning hair to look fuller. Fullora powders are all-natural, available in five varieties of shades and will not come off on clothing or on your pillowcase.</p>
    </div>
    <div class="ingredients"><strong>Ingredients</strong>Mica, Kaolin, Octyldodecyl Stearoyl Stearate, Synthetic Wax, Ethylhexyl Palmitate, Bis-Diglyceryl Polyacyladipate-2, Tocopheryl Acetate, Phenoxyethanol, Methylparaben, Propylparaben, Caprylyl Glycol, Ethylhexylglycerin, CI 77891, CI 77492, CI 77499, CI 77491</div>
    <div class="back-foot">
      <p class="warning">WARNING: Keep out of eyes. Stop use if irritation occurs. Keep out of reach of children.</p>
      <p class="address">Fullora Hair Powder 4210 Larkmoor Ave STE 12B<br>Brindle Springs, FL 30000<br>www.fullorahairdust.example</p>
    </div>
  </section>

  <section class="panel panel-front" aria-label="Box front panel">
    <div class="front-brand"><div class="name">Fullora</div><div class="sub">100% scalp coverage</div></div>
    <div class="front-compact" role="img" aria-label="Photo of the open silver compact with brown powder and applicator"></div>
    <ul class="claims"><li>TALC FREE</li><li>HAIR POWDER</li><li>EASY TO APPLY</li></ul>
    <div class="swatches" aria-label="Five shade swatches"><span class="s1"></span><span class="s2"></span><span class="s3"></span><span class="s4"></span><span class="s5"></span></div>
    <p class="availability">Available 5 Colors</p>
    <p class="net-weight">NET WT .32OZ /9g</p>
  </section>

  <div class="applicator-photo" role="img" aria-label="Photo of two sponge applicators with black handles"></div>
  <div class="product-photo" role="img" aria-label="Photo of the open silver powder compact with mirror, brown powder and sponge"></div>
</main>
</body>
</html>
```